Glow & Fizz Soiree for an Aesthetic practice

Please highlight creatively our event on 12/12/18 10AM-7PM at 8198 Jog RD Suite 104Boynton Beach FL 33419
RSVP at (561)-732-4085
*Velumyx Special $10 a unit (Bank your Velumyx for future treatments)
*20% off individual treatments or any DERMAVELLE products
*30% off package purchases
*Twice Sparkle- buy a gift card receive DOUBLE the amount up to $200
*Can't make it on 12/12/18- Call to schedule your appointment and prepay to lock in SPECIAL pricing
*Refer just 2 people or bring them as guests receive $100 worth of services or products FREE!!
* Food and Drinks
*Raffles
*Gift Bags
*Dermavelle Demos
Please use color scheme shown in Logo below
modern and feminine

Target Market(s)

Women and Men 25-65

Requirements
Must have
• R.O.E. Medical Weight Loss & Aesthetics
• address aand time above
Nice to have
• bubbles with specials inside

```html
<!DOCTYPE html>
<html lang="en">
<head>
<meta charset="utf-8">
<title>Glow &amp; Fizz Soiree</title>
<link rel="stylesheet" href="https://fonts.googleapis.com/css2?family=Fredoka:wght@400&family=Ubuntu:wght@300;400&family=Kaushan+Script&display=swap">
<style>
  :root {
    --slate: #3f4550;
    --teal: #6cc5cc;
    --cream: #fafaf8;
    --ink: #3b414b;
    --white: #ffffff;
    --logo-light: #e6e9ec;
  }
  html, body { margin: 0; padding: 0; overflow: hidden; background: var(--slate); }
  .flyer {
    position: relative;
    width: 851px;
    height: 1200px;
    overflow: hidden;
    background: var(--slate);
    font-family: "Ubuntu", sans-serif;
  }
  .backdrop { position: absolute; inset: 0; }
  .txt { position: absolute; margin: 0; white-space: nowrap; }

  .event-date, .event-time, .address, .rsvp {
    font-family: "Fredoka", sans-serif;
    font-weight: 400;
  }
  .event-date { left: 0; width: 464px; text-align: center; top: 32px; font-size: 50px; line-height: 50px; color: var(--ink); }
  .event-time { left: 0; width: 464px; text-align: center; top: 86px; font-size: 56px; line-height: 56px; color: var(--teal); letter-spacing: 1px; }
  .address { left: 46px; top: 174px; font-size: 42px; line-height: 47px; color: var(--teal); }
  .address .label { color: var(--ink); }
  .rsvp { left: 0; width: 420px; text-align: center; top: 346px; font-size: 34px; line-height: 38px; color: var(--ink); }
  .rsvp .phone { color: var(--teal); display: block; }

  .brand {
    position: absolute; left: 600px; top: 110px; width: 240px;
    font-family: "Ubuntu", sans-serif; font-weight: 300; color: var(--logo-light);
  }
  .brand-name { display: block; font-size: 76px; line-height: 80px; letter-spacing: 2px; }
  .brand-sub { display: block; font-size: 13px; line-height: 15px; text-transform: uppercase; margin-left: 100px; margin-top: 30px; white-space: normal; }

  .special { font-family: "Kaushan Script", cursive; color: var(--white); left: 40px; }
  .special .accent { color: var(--teal); }
  .special-title { top: 532px; font-size: 58px; line-height: 60px; color: var(--teal); }
  .special-line { font-size: 42px; line-height: 46px; }
  .special-line.l1 { top: 614px; }
  .special-line.l2 { top: 668px; }
  .special-line.l3 { top: 718px; }
  .special-line .price { font-size: 54px; }

  .perks {
    position: absolute; left: 546px; top: 342px; width: 296px; height: 388px;
    box-sizing: border-box; border: 5px solid var(--white);
    padding: 18px 10px 0 20px; color: var(--teal);
    font-size: 24px; line-height: 26.5px; font-weight: 300;
  }
  .perks p { margin: 0; }
  .perks .hi { color: var(--white); }
  .perks .referral { margin-bottom: 26px; }
  .perks .item { margin-bottom: 27.5px; }

  .discounts { left: 38px; top: 876px; font-size: 31px; line-height: 33px; color: var(--ink); font-weight: 400; }
  .discounts p { margin: 0 0 33px; }
  .discounts .hi { color: var(--white); }

  .gift { left: 544px; top: 828px; font-size: 36px; line-height: 38.5px; color: var(--teal); font-weight: 300; }
  .gift .dark { color: var(--ink); }
  .prepay { left: 508px; top: 1058px; font-size: 27px; line-height: 29px; color: var(--ink); font-weight: 300; }
</style>
</head>
<body>
<main class="flyer">
  <svg class="backdrop" width="851" height="1200" viewBox="0 0 851 1200" aria-hidden="true">
    <rect width="851" height="1200" fill="var(--slate)"/>
    <defs>
      <linearGradient id="wallTone" x1="0" y1="0" x2="1" y2="1">
        <stop offset="0" stop-color="#4a505b"/>
        <stop offset="1" stop-color="#2f343c"/>
      </linearGradient>
    </defs>
    <rect x="512" y="0" width="339" height="316" fill="url(#wallTone)" role="img" aria-label="Photo of the clinic wall behind the practice sign"/>
    <ellipse cx="200" cy="130" rx="352" ry="366" fill="var(--teal)"/>
    <ellipse cx="200" cy="140" rx="310" ry="302" fill="var(--cream)"/>
    <circle cx="96" cy="1064" r="252" fill="var(--white)"/>
    <circle cx="96" cy="1064" r="218" fill="var(--teal)"/>
    <circle cx="680" cy="1082" r="322" fill="var(--teal)"/>
    <circle cx="680" cy="1082" r="268" fill="var(--cream)"/>
  </svg>

  <h1 class="txt event-date">12/12/18</h1>
  <p class="txt event-time">10AM-7PM</p>
  <p class="txt address"><span class="label">at:</span> 4527 Marlow RD<br>Suite 208 Boynton<br>Beach FL 33419</p>
  <p class="txt rsvp">RSVP at:<span class="phone">(561)-732-4085</span></p>

  <div class="brand">
    <span class="brand-name">R.O.E.</span>
    <span class="brand-sub">Medical Weight Loss &amp; Aesthetics</span>
  </div>

  <h2 class="txt special special-title">Velumyx Special</h2>
  <p class="txt special special-line l1"><span class="accent price">$10</span> a unit (Bank</p>
  <p class="txt special special-line l2">your Velumyx for future</p>
  <p class="txt special special-line l3">treatments)</p>

  <section class="perks">
    <p class="referral">*Refer <span class="hi">just 2 people</span> or bring them as guests receive <span class="hi">$100</span> worth of services or products <span class="hi">FREE!!</span></p>
    <p class="item">* &nbsp;Food and Drinks</p>
    <p class="item">*Raffles</p>
    <p class="item">*Gift Bags</p>
    <p class="item">*Dermavelle Demos</p>
  </section>

  <div class="txt discounts">
    <p><span class="hi">*20% off</span><br>individual<br>treatments or<br>any <span class="hi">DERMAVELLE</span><br>products</p>
    <p><span class="hi">*30% off</span><br>package<br>purchases</p>
  </div>

  <p class="txt gift"><span class="dark">Twice Sparkle-</span><br>buy a gift card<br>receive <span class="dark">DOUBLE</span><br>the amount up to<br><span class="dark">$200</span></p>
  <p class="txt prepay">Can't make it on 12/12/18<br>Call to schedule your<br>appointment and prepay<br>to lock in SPECIAL pricing</p>
</main>
</body>
</html>
```